Business Card Design

I need a Business Card design completed with the attached logo. ***Cards will be printed on Clear Plastic Cards**** Design MUST be BOLD, Professional, and very VIBRANT!!!

Sentrix Halvoran is a trucking transport and logistics company serving the entire US. Our company prides itself on providing transportation, logistic services, and trucking jobs for Veterans. We strive for safe travels, efficient deliveries, maximum customer satisfaction, and continuous growth & improvement. Sentrix Halvoran offers stability, complete transparency and the ability to efficiently handle a vast majority of all transportation needs.

```html
<!DOCTYPE html>
<html lang="en">
<head>
<meta charset="utf-8">
<title>Sentrix Halvoran – Business Card</title>
<link rel="stylesheet" href="https://fonts.googleapis.com/css2?family=Arimo:wght@400;700&display=swap">
<style>
  :root {
    --page-bg: #e6e7ea;
    --card-frost: #f3f4f6;
    --card-frost-edge: #dfe1e5;
    --brand-blue: #233a97;
    --brand-blue-deep: #1b2d7c;
    --brand-gold: #d9a92c;
    --text-dark: #2c2f38;
    --text-light: #ffffff;
    --divider: #1f2f78;
  }
  * { box-sizing: border-box; margin: 0; padding: 0; }
  html, body {
    width: 1200px; height: 1015px; overflow: hidden;
    background: var(--page-bg);
    font-family: "Arimo", Arial, sans-serif;
  }
  .card {
    position: absolute; left: 60px; top: 208px;
    width: 1080px; height: 598px;
    background: linear-gradient(160deg, var(--card-frost), var(--card-frost-edge));
    box-shadow: 0 10px 30px rgba(0,0,0,.18);
    overflow: hidden;
  }
  .card-band { position: absolute; inset: 0; width: 100%; height: 100%; }
  .holder { position: absolute; left: 574px; top: 70px; width: 440px; text-align: center; }
  .holder-name { color: var(--brand-gold); font-weight: 700; font-size: 44px; line-height: 1.1; }
  .holder-title { color: var(--text-light); font-size: 27px; margin-top: 6px; }
  .company-name {
    position: absolute; left: 100px; top: 420px; width: 400px;
    text-align: center; color: var(--brand-gold);
    font-weight: 700; font-size: 40px; line-height: 1.15; letter-spacing: 1px;
  }
  .divider {
    position: absolute; left: 544px; top: 310px;
    width: 3px; height: 200px; background: var(--divider);
  }
  .contact { position: absolute; left: 614px; top: 308px; color: var(--text-dark); font-size: 23px; }
  .contact-address { line-height: 32px; margin-bottom: 22px; }
  .contact-list { list-style: none; }
  .contact-list li { display: flex; align-items: center; height: 32px; }
  .contact-icon { width: 18px; height: 18px; margin-right: 14px; flex: none; }
</style>
</head>
<body>
  <div class="card">
    <svg class="card-band" viewBox="0 0 1080 598" aria-hidden="true">
      <path d="M0 0 H1080 V188 C900 250 700 240 520 205 C340 170 160 160 0 190 Z" fill="var(--brand-blue)"/>
      <path d="M0 190 C160 160 340 170 520 205 C700 240 900 250 1080 188 V200 C900 262 700 252 520 218 C340 186 160 180 0 222 Z" fill="var(--brand-gold)"/>
      <path d="M520 205 C700 240 900 250 1080 188 V196 C900 256 700 246 520 212 Z" fill="var(--brand-blue-deep)" opacity=".5"/>
    </svg>

    <div class="holder">
      <p class="holder-name">Daniel Mercer</p>
      <p class="holder-title">President and CEO</p>
    </div>

    <p class="company-name">SENTRIX<br>HALVORAN</p>

    <div class="divider"></div>

    <div class="contact">
      <p class="contact-address">48 Harbour Lane, Kingsford<br>ON Canada K7L 2V4</p>
      <ul class="contact-list">
        <li>
          <svg class="contact-icon" viewBox="0 0 18 18"><rect x="5" y="1" width="8" height="16" rx="1.5" fill="none" stroke="var(--text-dark)" stroke-width="1.6"/><circle cx="9" cy="14" r="1" fill="var(--text-dark)"/></svg>
          (+1) 555 014 2263
        </li>
        <li>
          <svg class="contact-icon" viewBox="0 0 18 18"><path d="M4 1.5 L7 5 L5.5 7 C6.5 9.5 8.5 11.5 11 12.5 L13 11 L16.5 14 L14.5 16.5 C8 16 2 10 1.5 3.5 Z" fill="var(--text-dark)"/></svg>
          (+1) 555 014 2263
        </li>
        <li>
          <svg class="contact-icon" viewBox="0 0 18 18"><rect x="1" y="4" width="16" height="11" fill="none" stroke="var(--text-dark)" stroke-width="1.6"/><path d="M1 4 L9 10 L17 4" fill="none" stroke="var(--text-dark)" stroke-width="1.6"/></svg>
          hello@sentrixhalvoran.com
        </li>
        <li>
          <svg class="contact-icon" viewBox="0 0 18 18"><circle cx="9" cy="9" r="7.5" fill="none" stroke="var(--text-dark)" stroke-width="1.5"/><ellipse cx="9" cy="9" rx="3.2" ry="7.5" fill="none" stroke="var(--text-dark)" stroke-width="1.3"/><path d="M1.5 9 H16.5" stroke="var(--text-dark)" stroke-width="1.3"/></svg>
          www.sentrixhalvoran.com
        </li>
      </ul>
    </div>
  </div>
</body>
</html>
```